BRAVEK THERAPEUTICS

physical therapy company. need a flashy image and named logo, website link, that I can also use on Letterhead and business cards. Clean, sharp, modern, eye catching. 3 colors? Some shine. Needs to stand out and not be trendy or too much cursive . Androgynous image of a human body is ok. A spine included is ok. Prefer lines to curves for font types. Warm colors but strong impact. Will need to have some contact info and border mission statement on it.

Target Market(s)

Target market is large corporations, wealthy individuals, medical doctors

Industry/Entity Type

Medical, physical therapy

Contact Information for Business Card

Name, Owner, phone, email, and website

Colors
0054AA
0677BA
7BADD7
CADEEF
E8F1F8

Requirements
Must have
• See above- something about BALANCE, wellness, strength etc
Nice to have
• Contrast, depth
Should not have
• No cursive

```html
<!DOCTYPE html>
<html lang="en">
<head>
<meta charset="utf-8">
<title>Bravek Therapeutics – Business Card</title>
<link rel="stylesheet" href="https://fonts.googleapis.com/css2?family=Cinzel:wght@600&family=Poppins:wght@400&display=swap">
<style>
  :root {
    --brand-blue: #0054aa;
    --brand-blue-light: #3f7fc4;
    --bone-tone: #7badd7;
    --ink: #1e1e1e;
    --rule: #b9b9b9;
    --paper: #ffffff;
    --backdrop: #e4e6e9;
  }
  * { margin: 0; padding: 0; box-sizing: border-box; }
  html, body { width: 1093px; height: 1200px; overflow: hidden; }
  body { background: var(--backdrop); position: relative; font-family: "Poppins", sans-serif; }

  .card {
    position: absolute;
    left: 265px;
    width: 578px;
    height: 357px;
    border-radius: 26px;
    overflow: hidden;
  }
  .card--front { top: 226px; background: var(--paper); }
  .card--back  { top: 621px; background: var(--brand-blue); }

  .wordmark {
    position: absolute;
    font-family: "Cinzel", serif;
    font-weight: 600;
    text-align: center;
    line-height: 1;
    white-space: nowrap;
  }
  .wordmark__name { display: block; font-size: 50px; letter-spacing: 1px; }
  .wordmark__sub  { display: block; font-size: 29px; margin-top: 4px; letter-spacing: 0.5px; }

  .card--front .wordmark { left: 0; width: 290px; top: 140px; color: var(--brand-blue); }
  .card--back  .wordmark { left: 130px; width: 325px; top: 142px; color: var(--paper); }

  .divider {
    position: absolute;
    left: 288px; top: 95px;
    width: 1.5px; height: 168px;
    background: linear-gradient(to bottom, transparent, var(--rule) 15%, var(--rule) 85%, transparent);
  }

  .contact { position: absolute; left: 311px; top: 114px; }
  .contact__name {
    font-family: "Cinzel", serif; font-weight: 600;
    font-size: 21px; color: var(--brand-blue); line-height: 1;
  }
  .contact__role { font-size: 16.5px; color: var(--ink); line-height: 1.1; margin-top: 2px; }
  .contact__list { list-style: none; margin-top: 18px; }
  .contact__item {
    display: flex; align-items: center; gap: 8px;
    font-size: 17px; color: var(--ink); line-height: 22px;
  }
  .contact__item svg { width: 15px; height: 15px; flex: none; }
  .contact__accent { color: var(--brand-blue); }

  .figure-art {
    position: absolute;
    left: 40px; top: 6px;
    width: 130px; height: 346px;
    border-radius: 60px 60px 30px 30px;
    background: radial-gradient(ellipse at 50% 45%, rgba(123,173,215,0.45), rgba(123,173,215,0.12) 70%, transparent 100%);
  }
</style>
</head>
<body>

  <section class="card card--front" aria-label="Business card front">
    <div class="wordmark">
      <span class="wordmark__name">BRAVEK</span>
      <span class="wordmark__sub">THERAPEUTICS</span>
    </div>

    <div class="divider"></div>

    <div class="contact">
      <p class="contact__name">DANIEL MERCER</p>
      <p class="contact__role">Managing Director</p>
      <ul class="contact__list">
        <li class="contact__item">
          <svg viewBox="0 0 24 24" aria-hidden="true"><path fill="var(--brand-blue)" d="M6.6 10.8a15 15 0 0 0 6.6 6.6l2.2-2.2c.3-.3.7-.4 1-.2 1.1.4 2.3.6 3.6.6.6 0 1 .4 1 1V20c0 .6-.4 1-1 1A17 17 0 0 1 3 4c0-.6.4-1 1-1h3.5c.6 0 1 .4 1 1 0 1.3.2 2.5.6 3.6.1.3 0 .7-.2 1z"/></svg>
          044-555 210 347
        </li>
        <li class="contact__item">
          <svg viewBox="0 0 24 24" aria-hidden="true"><rect x="2" y="5" width="20" height="14" fill="var(--brand-blue)"/><path d="M2 5l10 8 10-8M2 19l7-6M22 19l-7-6" stroke="#fff" stroke-width="1.6" fill="none"/></svg>
          hello@bravekmail.com
        </li>
        <li class="contact__item">
          <svg viewBox="0 0 24 24" aria-hidden="true"><g fill="none" stroke="var(--brand-blue)" stroke-width="1.8"><circle cx="12" cy="12" r="9.5"/><ellipse cx="12" cy="12" rx="4.5" ry="9.5"/><path d="M2.5 12h19M4 7h16M4 17h16"/></g></svg>
          <span>www.<span class="contact__accent">bravektherapy</span>.com</span>
        </li>
      </ul>
    </div>
  </section>

  <section class="card card--back" aria-label="Business card back">
    <div class="figure-art" role="img" aria-label="Faint translucent illustration of a full human skeleton standing upright"></div>
    <div class="wordmark">
      <span class="wordmark__name">BRAVEK</span>
      <span class="wordmark__sub">THERAPEUTICS</span>
    </div>
  </section>

</body>
</html>
```